Disability and mental health support work company requires business card

Specialising
Wrenfield Disability is a new QCAP service aimed toward QCAP participants with a history of criminal justice, psychosocial/mental health, intellectual, and cognitive disabilities.

Our focus
Focusing on providing core QCAP supports for community participation, daily activities and supported independent living.

Authentic
Likeminded people wanting to make a difference in participant's lives.

Our aim to provide holistic and empowering supports targeted towards creating independence and guidance for all participants and families.
Over 35 years of experience working with people that have psychosocial, intellectual, and cognitive disabilities.

Industry/Entity Type

disability and mental health

Contact Information for Business Card

logo - business name

Colors
0054AA
0677BA
7BADD7
CADEEF
E8F1F8
FFF300
FFF600
FEFA6F
FFFEC7
FFFEE8

Requirements
Must have
• want double sided business cards(wont let me change it)
Should not have
• any disability related pictures

```html
<!DOCTYPE html>
<html lang="en">
<head>
<meta charset="utf-8">
<title>Wrenfield Disability — Business Card</title>
<link href="https://fonts.googleapis.com/css2?family=Playfair+Display:wght@700&family=Work+Sans:wght@400;500&display=swap" rel="stylesheet">
<style>
  :root {
    --backdrop: #9a9a9a;
    --card-navy: #0b2f5f;
    --sky: #8dbbe8;
    --gold: #f1b42f;
    --ink-light: #f3f6fb;
    --serif: "Playfair Display", Georgia, serif;
    --sans: "Work Sans", Arial, sans-serif;
  }
  * { box-sizing: border-box; margin: 0; padding: 0; }
  html, body { width: 1200px; height: 1050px; overflow: hidden; }
  body {
    background: var(--backdrop);
    display: flex;
    flex-direction: column;
    align-items: center;
    justify-content: center;
    gap: 56px;
  }
  .card {
    width: 760px;
    height: 434px;
    background: var(--card-navy);
    border-bottom: 4px solid var(--gold);
    border-right: 2px solid var(--gold);
    position: relative;
  }

  /* Details side */
  .card--details {
    display: flex;
    align-items: center;
    justify-content: center;
    gap: 56px;
  }
  .identity { text-align: right; }
  .identity__name {
    font-family: var(--serif);
    font-weight: 700;
    font-size: 30px;
    letter-spacing: 1px;
    color: var(--sky);
    text-transform: uppercase;
  }
  .identity__role {
    font-family: var(--sans);
    font-size: 15px;
    color: var(--gold);
    margin-top: 4px;
  }
  .identity__rule {
    width: 22px;
    height: 1px;
    background: var(--sky);
    margin: 14px 0 14px auto;
  }
  .identity__address {
    font-family: var(--sans);
    font-size: 15px;
    line-height: 1.45;
    color: var(--ink-light);
  }
  .contact { list-style: none; display: flex; flex-direction: column; gap: 8px; }
  .contact__item {
    display: flex;
    align-items: center;
    gap: 12px;
    font-family: var(--sans);
    font-size: 15px;
    color: var(--ink-light);
  }
  .contact__icon { width: 22px; height: 22px; flex: none; }

  /* Name side */
  .card--brand {
    display: flex;
    align-items: center;
    justify-content: center;
    gap: 18px;
  }
  .brand__dot {
    width: 26px;
    height: 26px;
    border-radius: 50%;
    background: var(--gold);
  }
  .brand__name {
    font-family: var(--serif);
    font-weight: 700;
    font-size: 50px;
    color: var(--sky);
  }
</style>
</head>
<body>
  <section class="card card--details" aria-label="Business card, contact side">
    <div class="identity">
      <h1 class="identity__name">Daniel Hartley</h1>
      <p class="identity__role">President</p>
      <div class="identity__rule"></div>
      <p class="identity__address">4120 Harbour Lane<br>Juneau, Alaska 34210</p>
    </div>
    <ul class="contact">
      <li class="contact__item">
        <svg class="contact__icon" viewBox="0 0 22 22" aria-hidden="true"><circle cx="11" cy="11" r="11" fill="#f1b42f"/><path d="M7.5 6.5l2 0 1 2.5-1.3 1a6 6 0 0 0 2.8 2.8l1-1.3 2.5 1 0 2c-4.5.5-8.5-3.5-8-8z" fill="#0b2f5f"/></svg>
        555-214-0186
      </li>
      <li class="contact__item">
        <svg class="contact__icon" viewBox="0 0 22 22" aria-hidden="true"><circle cx="11" cy="11" r="11" fill="#f1b42f"/><rect x="8" y="5.5" width="6" height="11" rx="1" fill="none" stroke="#0b2f5f" stroke-width="1.4"/><circle cx="11" cy="14.5" r=".7" fill="#0b2f5f"/></svg>
        555-418-0273
      </li>
      <li class="contact__item">
        <svg class="contact__icon" viewBox="0 0 22 22" aria-hidden="true"><circle cx="11" cy="11" r="11" fill="#f1b42f"/><rect x="6" y="7.5" width="10" height="7" fill="none" stroke="#0b2f5f" stroke-width="1.3"/><path d="M6 7.5l5 4 5-4" fill="none" stroke="#0b2f5f" stroke-width="1.3"/></svg>
        info@wrenfielddisability.com
      </li>
      <li class="contact__item">
        <svg class="contact__icon" viewBox="0 0 22 22" aria-hidden="true"><circle cx="11" cy="11" r="11" fill="#f1b42f"/><circle cx="11" cy="11" r="5" fill="none" stroke="#0b2f5f" stroke-width="1.3"/><ellipse cx="11" cy="11" rx="2" ry="5" fill="none" stroke="#0b2f5f" stroke-width="1.1"/><path d="M6 11h10" stroke="#0b2f5f" stroke-width="1.1"/></svg>
        wrenfielddisability.com
      </li>
    </ul>
  </section>

  <section class="card card--brand" aria-label="Business card, name side">
    <span class="brand__dot" aria-hidden="true"></span>
    <p class="brand__name">Wrenfield Disability</p>
  </section>
</body>
</html>
```